Design some Business Cards for Kestrel Works

I need a design for business cards. I have an existing logo.

I am a sole trader (work for myself) and I provide computer and IT technology support services to small businesses in Australia. I advise business owners on how to best use and manage their IT systems and computers and I provide onsite computer troubleshooting services.
The style should reflect the professional nature of my work.
I would likely favour a simpler and clean design.

The artwork needs to be:
Single sided (just the front of the card)
89mm x 54mm in size.
Full colour.
To be printed on white stock (paper)

Details that need to be included on the business cards are:
Logo
Name Milo Brennard
Email address milo@kestrelworks-mail.com.au
Phone number 0423 587 219

The exact details will be supplied at the end of the contest for the final artwork.
Final artwork would need to be print ready – I can provide examples of what they need to look like.

```html
<!DOCTYPE html>
<html lang="en">
<head>
<meta charset="utf-8">
<title>Kestrel Works – Business Card</title>
<link rel="stylesheet" href="https://fonts.googleapis.com/css2?family=Caladea:wght@400;700&display=swap">
<style>
  :root {
    --backdrop: #d2e0e4;
    --card: #ffffff;
    --accent: #2a8fd8;
    --bar-top: #0aa8e8;
    --bar-bottom: #0a6fcd;
    --text-muted: #6d6f72;
    --text-contact: #5a5c60;
    --brand-mark: #1f6fb8;
  }
  * { margin: 0; padding: 0; box-sizing: border-box; }
  html, body {
    width: 1194px;
    height: 1200px;
    overflow: hidden;
    background: var(--backdrop);
    font-family: "Caladea", "Cambria", Georgia, serif;
  }
  .canvas {
    position: relative;
    width: 1194px;
    height: 1200px;
  }
  .business-card {
    position: absolute;
    left: 342px;
    top: 179px;
    width: 530px;
    height: 843px;
    background: var(--card);
  }
  .accent-bar {
    position: absolute;
    right: 0;
    top: 0;
    width: 33px;
    height: 100%;
    background: linear-gradient(to bottom, var(--bar-top), var(--bar-bottom));
  }
  .identity {
    position: absolute;
    right: 75px;
    top: 52px;
    text-align: right;
  }
  .identity__name {
    font-size: 41px;
    font-weight: 700;
    color: var(--accent);
    line-height: 1.1;
    letter-spacing: 0.2px;
  }
  .identity__role {
    margin-top: 8px;
    font-size: 24px;
    font-weight: 700;
    color: var(--text-muted);
  }
  .brand {
    position: absolute;
    left: 61px;
    top: 573px;
    display: flex;
    align-items: center;
    gap: 18px;
  }
  .brand__symbol {
    width: 58px;
    height: 58px;
    border-radius: 50%;
    background: var(--brand-mark);
  }
  .brand__name {
    font-size: 36px;
    font-weight: 400;
    color: var(--brand-mark);
    line-height: 1;
  }
  .contact {
    position: absolute;
    left: 55px;
    top: 677px;
    list-style: none;
    font-size: 29px;
    line-height: 37.5px;
    color: var(--text-contact);
  }
</style>
</head>
<body>
  <main class="canvas">
    <article class="business-card">
      <div class="accent-bar"></div>

      <header class="identity">
        <h1 class="identity__name">Milo Brennard</h1>
        <p class="identity__role">Designation</p>
      </header>

      <div class="brand">
        <span class="brand__symbol"></span>
        <span class="brand__name">Kestrel Works</span>
      </div>

      <ul class="contact">
        <li class="contact__email">milo@kestrelworks-mail.com.au</li>
        <li class="contact__phone">0423 587 219</li>
        <li class="contact__web">www.kestrelworks.com.au</li>
      </ul>
    </article>
  </main>
</body>
</html>
```